Integrative Family Medicine Brochure needed

Looking for a very professional, clean, simple, minimalist, bold well designed brochure.
I am reestablishing my practice in a new town and looking for a new look. I am currently in the process of revising my corporate identity. I recently changed the business name to Brookvale Family Medicine.
You can visit the website http://brookvalefmclinic.example/ to get a feel for what I may be looking for. In the brochure I basically want excerpts from my home page, about, services and contact pages.
I have recently used Pixorama for both logo and business card and have been very happy, as soon as designs start being submitted I will switch to guaranteed payment.
"Brookvale" - similar font to "Cambria" and for "Family medicine" is "Trajan Pro"
I have attached several examples of brochures that have caught my eye to get the creative process started, but I am open to any design that conveys natural, life, health, and wellness.
Ideally colors would be muted or cool with emphasis on blues and greens
Feel free to use example stock photos in your design. I have attached the stock photos I have already purchased for the website.
Reason: Still waiting on a few more submissions, now that payment is guaranteed.
Target Market(s)
Health conscious people of all ages looking for a family medicine doctor
Industry/Entity Type
Town
Look and feel

```html
<!DOCTYPE html>
<html lang="en">
<head>
<meta charset="utf-8">
<title>Brookvale Family Medicine Brochure</title>
<link rel="stylesheet" href="https://fonts.googleapis.com/css2?family=Merriweather:wght@400;700&family=Noto+Serif:wght@400;700&display=swap">
<style>
:root{
  --stage:#000000;
  --paper:#ffffff;
  --paper-shade:#eceef0;
  --blue:#2e9fcd;
  --blue-deep:#1f7fae;
  --green:#6aa93c;
  --green-dark:#4f8f2a;
  --ink:#1c1c1c;
  --sky-top:#b9d8ef;
  --sky-low:#e8f2f8;
}
*{box-sizing:border-box;margin:0;padding:0}
html,body{width:800px;height:1200px;overflow:hidden;background:var(--stage)}
body{position:relative;font-family:"Noto Serif",Georgia,serif;color:var(--ink)}
.sheet{position:absolute;left:30px;width:740px;height:566px;background:linear-gradient(180deg,var(--paper) 0%,var(--paper-shade) 100%);overflow:hidden}
.sheet-outside{top:30px}
.sheet-inside{top:614px}
.panel{position:absolute;top:0;width:246.67px;height:100%}
.panel-1{left:0}.panel-2{left:246.67px}.panel-3{left:493.33px}
.heading{font-family:"Merriweather",Georgia,serif;font-weight:700;color:var(--blue);font-size:23px;letter-spacing:.3px}
.body-text{font-size:9.3px;line-height:12.1px}
.art{position:absolute;display:block}
/* outside */
.about .heading{position:absolute;left:14px;top:14px}
.about .body-text{position:absolute;left:14px;top:64px;width:218px}
.doctor-name{position:absolute;left:0;bottom:6px;width:100%;text-align:center;font-family:"Merriweather",serif;font-weight:700;font-size:16px}
.brand-name{font-family:"Merriweather",Georgia,serif;font-weight:700;color:var(--blue-deep);display:flex;align-items:center;gap:8px}
.brand-dot{width:14px;height:14px;border-radius:50%;background:var(--green);flex:none}
.contact .brand-name{position:absolute;left:16px;top:198px;font-size:33px}
.contact .heading{position:absolute;left:0;width:100%;text-align:center;top:270px;font-size:24px}
.address{position:absolute;left:0;width:100%;top:316px;text-align:center;font-weight:700;font-size:10.3px;line-height:14px}
.cover .brand-name{position:absolute;left:24px;top:44px;font-size:33px}
.tagline{position:absolute;left:0;width:100%;top:418px;text-align:center;color:#fff;font-family:"Merriweather",serif;line-height:20px}
.tagline strong{display:block;font-size:16.5px;font-weight:700}
.tagline span{display:block;font-size:13px;line-height:15.5px;font-family:"Noto Serif",serif}
.website{position:absolute;left:0;bottom:10px;width:100%;text-align:center;font-family:"Merriweather",serif;font-weight:700;font-size:12.5px}
/* inside */
.services .heading{position:absolute;left:14px;top:8px}
.service{position:absolute;left:14px;width:222px}
.service-title{display:flex;align-items:center;gap:8px;font-family:"Merriweather",serif;font-weight:700;color:var(--green);font-size:12.5px;margin-bottom:10px;line-height:14px}
.service-mark{width:12px;height:12px;border-radius:50%;background:var(--blue);flex:none}
.tick-list{list-style:none;font-size:9.6px;line-height:12.2px;padding-left:14px;margin-top:-2px}
.tick-list li{position:relative;padding-left:12px}
.tick-list li svg{position:absolute;left:0;top:2px}
</style>
</head>
<body>

<section class="sheet sheet-outside" aria-label="Brochure outside">
  <div class="panel panel-1 about">
    <h2 class="heading">ABOUT US</h2>
    <p class="body-text">My primary purpose is to get sick people well, and the way I feel this is best done is within the framework of Integrative Family Medicine. I believe medicine is much more than just dispensing pills and I take care of each patient as I would want my own family members to be treated. Many issues face us in our goal of leading a productive healthy life. We are living longer due to the improvement in public health, nutrition, and modern medicine. Yet in many ways we have become less healthy. Obesity, cancer, heart disease, Alzheimer's, autism, are consuming the population. Much of what we suffer from is self inflicted and based in a lack of discipline. We have been tricked into valuing the momentary pleasure instead of long lasting health. Our health is an amalgam of the air we breathe, food we eat, thoughts we think, which I have heard put another way, "Health is what we do for our body minus what we do to our body." Some people come to the doctor looking for the magic pill or to be fixed blaming doctors when they don't get better, going through a long list of treatments they have done, yet are still smoking, not exercising, eating junk food, and overweight.</p>
    <svg class="art" style="left:66px;top:420px" width="120" height="140" viewBox="0 0 120 140" role="img" aria-label="Portrait photo of the doctor">
      <defs><linearGradient id="portrait" x1="0" y1="0" x2="0" y2="1"><stop offset="0" stop-color="#d9d5cf"/><stop offset="1" stop-color="#bfb3a6"/></linearGradient></defs>
      <rect width="120" height="140" fill="url(#portrait)"/>
    </svg>
    <svg class="art" style="left:0;top:520px" width="247" height="46" viewBox="0 0 247 46" aria-hidden="true">
      <path d="M0 14 Q120 -4 247 16 V46 H0 Z" fill="#fff"/>
      <path d="M0 14 Q120 -4 247 16" fill="none" stroke="var(--green)" stroke-width="4"/>
    </svg>
    <div class="doctor-name">Dr Harlow</div>
  </div>

  <div class="panel panel-2 contact">
    <svg class="art" style="left:0;top:0" width="247" height="140" viewBox="0 0 247 140" role="img" aria-label="Photo of a woman in white raising her arms under a blue sky">
      <defs><linearGradient id="sky" x1="0" y1="0" x2="0" y2="1"><stop offset="0" stop-color="var(--sky-top)"/><stop offset="1" stop-color="var(--sky-low)"/></linearGradient></defs>
      <path d="M0 0 H247 V104 Q180 132 120 120 Q60 106 0 122 Z" fill="url(#sky)"/>
      <path d="M120 120 Q180 132 247 104" fill="none" stroke="var(--blue)" stroke-width="3"/>
    </svg>
    <div class="brand-name"><span class="brand-dot"></span>Brookvale</div>
    <h2 class="heading">CONTACT US</h2>
    <p class="address">Address: 418 Ridgeline Parkway<br>West, Brookvale Texas 79000<br>Telephone: (555) 210-4830<br>FAX: (555) 210-4831</p>
    <svg class="art" style="left:0;top:420px" width="247" height="146" viewBox="0 0 247 146" role="img" aria-label="Street map showing the clinic location">
      <path d="M0 14 Q120 -6 247 12 V146 H0 Z" fill="#efe9dc"/>
      <path d="M0 14 Q120 -6 247 12" fill="none" stroke="var(--blue)" stroke-width="4"/>
    </svg>
  </div>

  <div class="panel panel-3 cover">
    <div class="brand-name"><span class="brand-dot"></span>Brookvale</div>
    <svg class="art" style="left:0;top:104px" width="247" height="320" viewBox="0 0 247 320" role="img" aria-label="Photo of a happy couple leaping together in a sunny field">
      <defs><linearGradient id="meadow" x1="0" y1="0" x2="0" y2="1"><stop offset="0" stop-color="#cfe3f2"/><stop offset=".75" stop-color="#f3f7f9"/><stop offset="1" stop-color="#a9c98a"/></linearGradient></defs>
      <path d="M0 24 Q110 -6 247 22 V320 H0 Z" fill="url(#meadow)"/>
      <path d="M0 24 Q110 -6 247 22" fill="none" stroke="var(--blue)" stroke-width="3"/>
    </svg>
    <svg class="art" style="left:0;top:396px" width="247" height="134" viewBox="0 0 247 134" aria-hidden="true">
      <path d="M0 18 Q140 -4 247 10 V134 H0 Z" fill="var(--green)"/>
    </svg>
    <div class="tagline"><strong>RESTORING YOUR<br>HEALTH NATURALLY</strong><span>with<br>Nutrition, Manipulation,<br>Acupuncture, and Integrative<br>Medicine</span></div>
    <svg class="art" style="left:0;top:520px" width="247" height="46" viewBox="0 0 247 46" aria-hidden="true">
      <path d="M0 14 Q120 -4 247 10 V46 H0 Z" fill="#fff"/>
    </svg>
    <div class="website">www.brookvalefmclinic.example</div>
  </div>
</section>

<section class="sheet sheet-inside" aria-label="Brochure inside">
  <div class="panel panel-1 services">
    <h2 class="heading">OUR SERVICES</h2>
    <div class="service" style="top:52px">
      <h3 class="service-title"><span class="service-mark"></span>Family Medicine</h3>
      <p class="body-text">Routine primary care is provided for newborns to adults. We do everything that a primary care practice does plus we deliver it in an integrative way. This includes routine physicals, gynecological care (including pap smears), same day visits for acute conditions, and chronic disease management. A network of specialists and other providers are available, which supports an integrative approach.</p>
    </div>
    <div class="service" style="top:224px">
      <h3 class="service-title"><span class="service-mark"></span>Manipulation</h3>
      <p class="body-text">Dr. Harlow has been trained as an Osteopathic Physician and, as such, has been trained in manual manipulation. He had learned about manipulation, long before medical school, as his father is a chiropractor. He has studied with some of this country's best doctors, who specialize in manipulation, and has attended many courses and conferences regarding manipulation, and utilizes many different techniques, from cranial treatments to high velocity adjustments.</p>
    </div>
  </div>

  <div class="panel panel-2">
    <div class="service" style="top:20px">
      <h3 class="service-title"><span class="service-mark"></span>Nutrition</h3>
      <p class="body-text">Having a bachelor's degree in Nutritional Science, Dr. Harlow has the conviction that nutrition is one of the keys to optimal health, since nutrition has an effect on one's body every day. Nutrition is not traditionally taught in medical schools, so many physicians fall short in treatment of many chronic conditions, as most medications are not designed for long-term therapy.</p>
    </div>
    <svg class="art" style="left:160px;top:8px" width="70" height="40" viewBox="0 0 70 40" role="img" aria-label="Photo of a blueberry on a leaf">
      <rect width="70" height="40" rx="6" fill="#7c9a5a"/>
    </svg>
    <div class="service" style="top:188px">
      <h3 class="service-title"><span class="service-mark"></span>Acupuncture</h3>
      <ul class="tick-list">
        <li><svg width="10" height="9" viewBox="0 0 10 9" aria-hidden="true"><path d="M1 5 L4 8 L9 1" fill="none" stroke="var(--blue)" stroke-width="2"/></svg>Auricular Acupuncture</li>
        <li><svg width="10" height="9" viewBox="0 0 10 9" aria-hidden="true"><path d="M1 5 L4 8 L9 1" fill="none" stroke="var(--blue)" stroke-width="2"/></svg>Chinese Scalp Acupuncture</li>
        <li><svg width="10" height="9" viewBox="0 0 10 9" aria-hidden="true"><path d="M1 5 L4 8 L9 1" fill="none" stroke="var(--blue)" stroke-width="2"/></svg>Energetic Acupuncture</li>
        <li><svg width="10" height="9" viewBox="0 0 10 9" aria-hidden="true"><path d="M1 5 L4 8 L9 1" fill="none" stroke="var(--blue)" stroke-width="2"/></svg>Five Element Constitutional Acupuncture</li>
        <li><svg width="10" height="9" viewBox="0 0 10 9" aria-hidden="true"><path d="M1 5 L4 8 L9 1" fill="none" stroke="var(--blue)" stroke-width="2"/></svg>Pain Management</li>
        <li><svg width="10" height="9" viewBox="0 0 10 9" aria-hidden="true"><path d="M1 5 L4 8 L9 1" fill="none" stroke="var(--blue)" stroke-width="2"/></svg>Percutaneous Nerve Stimulation</li>
      </ul>
    </div>
    <div class="service" style="top:316px">
      <h3 class="service-title"><span class="service-mark"></span>Prolotherapy</h3>
      <p class="body-text">Dr Harlow was first introduced to prolotherapy in medical school. After seeing the potential benefits it could offer a patient suffering with pain, he has sought out training in prolotherapy.</p>
    </div>
  </div>

  <div class="panel panel-3">
    <div class="service" style="top:20px">
      <h3 class="service-title"><span class="service-mark"></span>Bio-Identical Hormone<br>Replacement</h3>
      <p class="body-text">Bio-Identical Hormone replacement is based on the principle that hormone replacement should mimic our natural hormone production as closely as possible. Hormone replacement should, ideally, reproduce the exact same hormonal milieu that is present in a healthy, youthful patient.</p>
    </div>
    <div class="service" style="top:158px">
      <h3 class="service-title"><span class="service-mark"></span>Allergy Testing</h3>
      <p class="body-text">We offer both traditional allergy injections and oral drops. If you choose the oral drops, you will have no more time-consuming trips to the doctor for injections! Our advanced allergy treatment allows you to easily take the oral solution at home as drops under the tongue, rather than by injections.</p>
    </div>
    <div class="service" style="top:286px">
      <h3 class="service-title"><span class="service-mark"></span>Labs</h3>
      <p class="body-text">We can do in-house phlebotomy. In addition to ordering conventional labs through your insurance company (usually Meridian or LabNova), we also offer many alternative laboratory evaluations. Testing available includes digestive studies, food sensitivities, antioxidant and nutritional deficiencies evaluation, hormonal and heavy metal levels, etc.</p>
    </div>
  </div>

  <svg class="art" style="left:0;top:424px" width="740" height="142" viewBox="0 0 740 142" aria-hidden="true">
    <defs>
      <linearGradient id="family" x1="0" y1="0" x2="1" y2="1"><stop offset="0" stop-color="#e9c9a8"/><stop offset="1" stop-color="#c08f6a"/></linearGradient>
      <linearGradient id="needles" x1="0" y1="0" x2="0" y2="1"><stop offset="0" stop-color="#1a1410"/><stop offset="1" stop-color="#6b4a34"/></linearGradient>
      <linearGradient id="allergy" x1="0" y1="0" x2="1" y2="0"><stop offset="0" stop-color="#6f9a3c"/><stop offset="1" stop-color="#e6d3b8"/></linearGradient>
    </defs>
    <path role="img" aria-label="Photo of a smiling family" d="M0 8 Q120 -2 247 12 V142 H0 Z" fill="url(#family)"/>
    <path role="img" aria-label="Photo of acupuncture needles on a patient's back" d="M247 12 Q370 0 494 12 V142 H247 Z" fill="url(#needles)"/>
    <path role="img" aria-label="Photo of a woman with allergies using a tissue" d="M494 12 Q620 2 740 14 V142 H494 Z" fill="url(#allergy)"/>
    <path d="M0 8 Q120 -2 247 12 Q370 0 494 12 Q620 2 740 14" fill="none" stroke="var(--blue)" stroke-width="3"/>
  </svg>
</section>

</body>
</html>
```